Business Card For Kelmora Financial Consulting

Hi, I would like a business card designed. Bold, modern.
Please use the same design as the logo. I have also attached the website design to see the overall theme.
Wordmark Font
Color: Hex: #01AEF7

```html
<!DOCTYPE html>
<html lang="en">
<head>
<meta charset="UTF-8">
<title>Kelmora Financial Consulting – Business Card</title>
<link rel="stylesheet" href="https://fonts.googleapis.com/css2?family=Montserrat:wght@400;600&display=swap">
<style>
  :root {
    --page-bg: #f4f4f4;
    --card-navy: #1a2836;
    --brand-blue: #01aef7;
    --brand-blue-deep: #0b7fc0;
    --text-light: #e6edf3;
    --text-muted: #b9c5d0;
  }
  * { margin: 0; padding: 0; box-sizing: border-box; }
  html, body {
    width: 900px; height: 1200px; overflow: hidden;
    background: var(--page-bg);
    font-family: "Montserrat", sans-serif;
  }
  .stage {
    width: 900px; height: 1200px;
    display: flex; align-items: center; justify-content: center;
  }
  .business-card {
    position: relative;
    width: 760px; height: 434px;
    background: var(--card-navy);
    overflow: hidden;
    box-shadow: 0 10px 30px rgba(0,0,0,0.15);
  }
  .accent { position: absolute; inset: 0; width: 100%; height: 100%; }
  .brand {
    position: absolute; left: 150px; top: 76px;
    display: flex; align-items: center; gap: 12px;
  }
  .brand-dot {
    width: 16px; height: 16px; border-radius: 50%;
    background: var(--brand-blue);
  }
  .brand-name {
    color: var(--text-light);
    font-weight: 600; font-size: 24px; line-height: 1;
  }
  .contact-list {
    position: absolute; left: 150px; top: 196px;
    list-style: none; color: var(--text-muted);
    font-size: 15px; line-height: 1.45;
  }
  .contact-item { display: flex; gap: 14px; margin-bottom: 18px; }
  .contact-icon { flex: 0 0 18px; width: 18px; height: 18px; margin-top: 2px; }
</style>
</head>
<body>
<main class="stage">
  <section class="business-card" aria-label="Kelmora Financial Consulting business card">
    <svg class="accent" viewBox="0 0 760 434" preserveAspectRatio="none" aria-hidden="true">
      <polygon points="662,0 760,0 760,150" fill="var(--brand-blue)"/>
      <polygon points="700,0 760,0 760,70" fill="var(--brand-blue-deep)"/>
      <polygon points="0,290 0,434 112,434" fill="var(--brand-blue)"/>
      <polygon points="0,370 0,434 48,434" fill="var(--brand-blue-deep)"/>
    </svg>

    <div class="brand">
      <span class="brand-dot" aria-hidden="true"></span>
      <span class="brand-name">Kelmora Financial Consulting</span>
    </div>

    <ul class="contact-list">
      <li class="contact-item">
        <svg class="contact-icon" viewBox="0 0 24 24" aria-hidden="true"><path d="M6.6 10.8a15.1 15.1 0 0 0 6.6 6.6l2.2-2.2a1 1 0 0 1 1-.25 11.4 11.4 0 0 0 3.6.57 1 1 0 0 1 1 1V20a1 1 0 0 1-1 1A17 17 0 0 1 3 4a1 1 0 0 1 1-1h3.5a1 1 0 0 1 1 1c0 1.25.2 2.45.57 3.57a1 1 0 0 1-.25 1z" fill="var(--brand-blue)"/></svg>
        <span>+1 000 000 0000</span>
      </li>
      <li class="contact-item">
        <svg class="contact-icon" viewBox="0 0 24 24" aria-hidden="true"><path d="M12 2a7 7 0 0 0-7 7c0 5.2 7 13 7 13s7-7.8 7-13a7 7 0 0 0-7-7zm0 9.5A2.5 2.5 0 1 1 12 6.5a2.5 2.5 0 0 1 0 5z" fill="var(--brand-blue)"/></svg>
        <span>000 Lorem ipsum dolor sit amet,<br>consectetur adipiscing elit, sed<br>United States, State, Zip code</span>
      </li>
      <li class="contact-item">
        <svg class="contact-icon" viewBox="0 0 24 24" aria-hidden="true"><circle cx="12" cy="12" r="9" fill="none" stroke="var(--brand-blue)" stroke-width="2"/><path d="M3 12h18M12 3c3 3.5 3 14.5 0 18M12 3c-3 3.5-3 14.5 0 18" fill="none" stroke="var(--brand-blue)" stroke-width="1.6"/></svg>
        <span>Website: Kelmoraconsulting.com<br>info@kelmoraconsulting.com</span>
      </li>
    </ul>
  </section>
</main>
</body>
</html>
```